I have a logo and need to design the business card and stationery.
Updates

The uploaded logo image named as GREYHAVEN CONSTRUCTION which is to be replaced to GREYHAVEN CONTRACTS. Kindly add below details and submit the designs- Company name- Greyhaven Engineering Contracts LLP Name & Post- Kunal Mehra (Designated Partner) Address- Block No.317, Wing C, Tulsi Trade Plaza, Lokhand Marg, Varun Industrial Park, Goregaon(E), Mumbai - 400 063 Contact- +91 97410 58723 Email- kunalmehra@examplemail.com Website- www.greyhavencontracts.example Contact for Letterhead- +91-22-28145597

Hi Tanvir Rahman, We are liking your Design #41927506. We have suggested some changes which are mentioned in feedback. Kindly revert with it asap to finalize this design.

Colors

Designer to choose colors to be used in the design.

```html
<!DOCTYPE html>
<html lang="en">
<head>
<meta charset="utf-8">
<title>Greyhaven Contracts – Business Card</title>
<link href="https://fonts.googleapis.com/css2?family=Montserrat:wght@300;400;700&display=swap" rel="stylesheet">
<style>
  :root {
    --backdrop: #b9b7b5;
    --card-dark: #141414;
    --card-dark-block: #1f1f1f;
    --card-dark-mark: #4a4a4a;
    --card-light: #efefef;
    --card-light-block: #e3e3e3;
    --ink: #1a1a1a;
    --ink-soft: #3a3a3a;
    --paper-text: #f2f2f2;
  }
  * { margin: 0; padding: 0; box-sizing: border-box; }
  html, body {
    width: 1200px; height: 1014px; overflow: hidden;
    background: var(--backdrop);
    font-family: "Montserrat", sans-serif;
  }
  .card {
    position: absolute;
    left: 337px;
    width: 525px; height: 290px;
    overflow: hidden;
    box-shadow: 0 6px 18px rgba(0,0,0,0.25);
  }
  .card--back { top: 208px; background: var(--card-dark); }
  .card--front { top: 516px; background: var(--card-light); }

  .card__block {
    position: absolute;
    left: 294px; top: 22px;
    width: 231px; height: 246px;
  }
  .card--back .card__block { background: var(--card-dark-block); }
  .card--front .card__block { background: var(--card-light-block); }

  .address {
    position: absolute;
    left: 0; width: 296px; top: 114px;
    text-align: center;
    color: var(--paper-text);
    font-weight: 300;
    font-size: 10.5px;
    line-height: 12.5px;
  }
  .address__pin { display: block; margin: 0 auto 8px; }

  .brand {
    position: absolute;
    left: 42px; width: 160px; top: 38px;
    text-align: center;
    color: var(--ink);
    font-weight: 700;
  }
  .brand__square {
    display: block;
    width: 46px; height: 46px;
    margin: 0 auto 10px;
    background: var(--ink);
  }
  .brand__name { font-size: 14px; letter-spacing: 0.5px; line-height: 16px; }
  .brand__sub { font-size: 8px; letter-spacing: 4px; line-height: 11px; }

  .person {
    position: absolute; left: 42px; top: 152px;
    color: var(--ink);
  }
  .person__name { font-size: 19px; line-height: 22px; }
  .person__first { font-weight: 700; }
  .person__last { font-weight: 300; }
  .person__role { font-size: 11px; font-weight: 300; color: var(--ink-soft); margin-top: 1px; }

  .contacts {
    position: absolute; left: 42px; top: 202px;
    list-style: none;
    font-size: 11.5px; font-weight: 300; color: var(--ink);
  }
  .contacts li { display: flex; align-items: center; height: 18px; }
  .contacts svg { margin-right: 6px; flex: none; }
</style>
</head>
<body>
  <section class="card card--back">
    <div class="address">
      <svg class="address__pin" width="14" height="18" viewBox="0 0 14 18">
        <path d="M7 1a5 5 0 0 0-5 5c0 4 5 9 5 9s5-5 5-9a5 5 0 0 0-5-5z" fill="none" stroke="#f2f2f2" stroke-width="1.5"/>
        <circle cx="7" cy="6" r="1.8" fill="none" stroke="#f2f2f2" stroke-width="1.3"/>
        <path d="M3 16.5h8" stroke="#f2f2f2" stroke-width="1.3"/>
      </svg>
      Block No.317, Wing C, Tulsi Trade Plaza,<br>
      Lokhand Marg, Varun Industrial Park,<br>
      Goregaon(E), Mumbai - 400 063
    </div>
    <div class="card__block"></div>
  </section>

  <section class="card card--front">
    <div class="brand">
      <span class="brand__square"></span>
      <div class="brand__name">GREYHAVEN</div>
      <div class="brand__sub">CONTRACTS</div>
    </div>

    <div class="person">
      <div class="person__name"><span class="person__first">Kunal</span> <span class="person__last">Mehra</span></div>
      <div class="person__role">(Designated Partner)</div>
    </div>

    <ul class="contacts">
      <li>
        <svg width="12" height="12" viewBox="0 0 12 12"><circle cx="6" cy="6" r="6" fill="#1a1a1a"/><path d="M4 3.2l1 1.4-.6.7c.4.9 1.1 1.6 2 2l.7-.6 1.4 1-.5 1c-2.3-.2-4.3-2.2-4.5-4.5z" fill="#efefef"/></svg>
        +91 97410 58723
      </li>
      <li>
        <svg width="12" height="12" viewBox="0 0 12 12"><circle cx="6" cy="6" r="6" fill="#1a1a1a"/><rect x="3" y="4" width="6" height="4" fill="#efefef"/><path d="M3 4l3 2.2L9 4" fill="none" stroke="#1a1a1a" stroke-width="0.8"/></svg>
        kunalmehra@examplemail.com
      </li>
      <li>
        <svg width="12" height="12" viewBox="0 0 12 12"><circle cx="6" cy="6" r="5.4" fill="none" stroke="#1a1a1a" stroke-width="1.1"/><ellipse cx="6" cy="6" rx="2.2" ry="5.4" fill="none" stroke="#1a1a1a" stroke-width="0.9"/><path d="M0.8 6h10.4M1.8 3.5h8.4M1.8 8.5h8.4" stroke="#1a1a1a" stroke-width="0.8"/></svg>
        www.greyhavencontracts.example
      </li>
    </ul>
    <div class="card__block"></div>
  </section>
</body>
</html>
```